New iOS App design for Boston Startup

We are looking for a new app design for our Zorvak app. The current app's design feels outdated and we like to add lots of new functionality and a new navigation as well. A complete overhaul therefore!
We want you to design 5 screens that will have changed the most. The complete wireframes of these 5 pages are attached in the requirements document.
Once the winning design is selected we will award the winner with the designing all other screens (40-50 screens based on the same design). This will be a separate project worth $1000. The winning designer can get more follow up work if both sides are happy about the cooperation.
We will give feedback as soon as the first screen has been uploaded for review. Final decision will be made only after all 5 screens are finished.
We hope you give it your best!
Note: will only communicate through PixelGuild (no skype),
Updates
Project Deadline Extended
Reason: Want to give designers a chance to submit their designs as I understand from some, the deadline is too close.
I have raised the award and introduced a 2nd price as well to make it worth your time. I hope you give it your best shot.
Project Deadline Extended
Reason: A few of you have asked for an extension of the deadline as time is running out. I will extend by one day. Tell me if you need more.
Industry/Entity Type
Startup
Requirements
Must have
- At least 1 screen before we can give you feedback.
Nice to have
- multiple options of 1 screen to get to a desirable design

```html
<!DOCTYPE html>
<html lang="en">
<head>
<meta charset="utf-8">
<title>Zorvak – Home</title>
<link rel="stylesheet" href="https://fonts.googleapis.com/css2?family=Arimo:wght@400;700&display=swap">
<style>
  :root {
    --coral: #ef5050;
    --coral-dark: #c93c3c;
    --black: #000000;
    --tab-bg: #111111;
    --tab-text: #8a8a8a;
    --white: #ffffff;
    --sky-top: #8fb0cf;
    --sky-mid: #5f86ad;
    --sky-deep: #3d628c;
    --strip: rgba(232, 238, 245, 0.88);
    --strip-text: #333333;
    --divider: #dedede;
    --green: #45c052;
    --blue: #55a9ea;
    --amber: #f8b12a;
    --up: #3cb04a;
    --down: #e63b3b;
  }
  * { box-sizing: border-box; margin: 0; padding: 0; }
  html, body { width: 676px; height: 1200px; overflow: hidden; background: var(--white); }
  body { font-family: "Arimo", Arial, sans-serif; position: relative; }

  .status-bar { position: absolute; left: 0; top: 0; width: 676px; height: 42px; background: var(--black); color: var(--white); font-size: 23px; font-weight: 700; }
  .status-bar .carrier { position: absolute; left: 8px; top: 9px; display: flex; align-items: flex-end; gap: 6px; }
  .status-bar .time { position: absolute; left: 0; width: 676px; top: 9px; text-align: center; }
  .status-bar .right { position: absolute; right: 10px; top: 9px; display: flex; gap: 12px; align-items: center; }

  .app-header { position: absolute; left: 0; top: 42px; width: 676px; height: 93px; background: var(--coral); border-bottom: 2px solid var(--coral-dark); }
  .app-header .menu { position: absolute; left: 26px; top: 28px; }
  .app-header h1 { position: absolute; left: 154px; top: 24px; font-weight: 400; font-size: 39px; color: var(--white); }

  .profile { position: absolute; left: 0; top: 135px; width: 676px; height: 301px;
    background: linear-gradient(135deg, var(--sky-top) 0%, var(--sky-mid) 45%, var(--sky-deep) 100%); }
  .avatar { position: absolute; left: 17px; top: 39px; width: 190px; height: 190px; border-radius: 50%; border: 5px solid var(--white);
    background: radial-gradient(circle at 50% 40%, #b08a76 0%, #7c6658 55%, #c9d3dc 100%); }
  .profile .name { position: absolute; left: 241px; top: 58px; font-size: 43px; font-weight: 700; color: var(--white); }
  .profile .location { position: absolute; left: 241px; top: 112px; font-size: 27px; color: var(--white); display: flex; align-items: center; gap: 8px; }
  .profile .score { position: absolute; left: 239px; top: 172px; display: flex; align-items: baseline; color: var(--white); }
  .score .label { font-size: 43px; margin-right: 14px; }
  .score .value { font-size: 53px; color: var(--black); }
  .score .delta { font-size: 23px; margin-left: 10px; }

  .week-stats { position: absolute; left: 0; top: 436px; width: 676px; height: 99px; background: var(--strip); color: var(--strip-text); }
  .stat { position: absolute; top: 0; height: 99px; }
  .stat .num { position: absolute; top: 12px; font-size: 33px; color: var(--black); white-space: nowrap; display: flex; align-items: center; }
  .stat .cap { position: absolute; top: 56px; font-size: 27px; white-space: nowrap; }
  .week-stats .sep { position: absolute; top: 0; width: 1px; height: 99px; background: #555; }
  .progress { position: absolute; left: 0; top: 535px; width: 526px; height: 10px; background: var(--coral); }
  .progress-rest { position: absolute; left: 526px; top: 535px; width: 150px; height: 4px; background: var(--black); }

  .quick-links { position: absolute; left: 0; top: 545px; width: 676px; height: 282px; }
  .bubble-btn { position: absolute; top: 52px; width: 186px; height: 186px; border-radius: 50%; border: 4px solid var(--white);
    box-shadow: 3px 4px 4px rgba(0,0,0,0.55); color: var(--white); font-size: 30px; text-align: center; line-height: 1.22;
    display: flex; align-items: center; justify-content: center; }
  .bubble-btn span { display: block; margin-top: -12px; }
  .bubble-btn svg { position: absolute; left: 80px; bottom: 22px; }
  .btn-analytics { left: 25px; background: var(--green); }
  .btn-course { left: 247px; background: var(--blue); }
  .btn-days { left: 466px; background: var(--amber); }
  .rule { position: absolute; left: 0; width: 676px; height: 3px; background: var(--divider); }

  .up-next { position: absolute; left: 225px; top: 870px; }
  .up-next .text { position: absolute; left: 0; top: 0; width: 436px; height: 142px; text-align: center; color: var(--white); padding-top: 36px; }
  .up-next .kicker { font-size: 28px; }
  .up-next .lesson { font-size: 36px; margin-top: 8px; }

  .tab-bar { position: absolute; left: 0; top: 1064px; width: 676px; height: 136px; background: var(--tab-bg); border-top: 3px solid #444; }
  .tab { position: absolute; top: 0; width: 108px; height: 136px; color: var(--tab-text); font-size: 21px; text-align: center; }
  .tab svg { position: absolute; left: 27px; top: 26px; }
  .tab .label { position: absolute; left: 0; width: 100%; top: 100px; }
  .tab.active { background: var(--coral); color: var(--white); top: 15px; height: 121px; }
  .tab.active svg { top: 12px; }
  .tab.active .label { top: 86px; }
</style>
</head>
<body>
  <div class="status-bar">
    <div class="carrier">
      <svg width="34" height="20" viewBox="0 0 34 20"><rect x="0" y="15" width="5" height="5" fill="#fff"/><rect x="7" y="11" width="5" height="9" fill="#fff"/><rect x="14" y="7" width="5" height="13" fill="#fff"/><rect x="21" y="3" width="5" height="17" fill="#fff"/><rect x="28" y="0" width="5" height="20" fill="#777"/></svg>
      <span>ORBIT &nbsp;3G</span>
    </div>
    <div class="time">9:51 PM</div>
    <div class="right">
      <svg width="22" height="22" viewBox="0 0 22 22"><circle cx="11" cy="11" r="10" fill="#fff"/><path d="M11 5v6h4" stroke="#000" stroke-width="2" fill="none"/></svg>
      <svg width="44" height="22" viewBox="0 0 44 22"><rect x="1" y="2" width="38" height="18" rx="2" fill="none" stroke="#fff" stroke-width="2"/><rect x="4" y="5" width="32" height="12" fill="#fff"/><rect x="40" y="7" width="3" height="8" fill="#fff"/></svg>
    </div>
  </div>

  <header class="app-header">
    <svg class="menu" width="48" height="38" viewBox="0 0 48 38"><rect y="0" width="48" height="7" rx="2" fill="#fff"/><rect y="15" width="48" height="7" rx="2" fill="#fff"/><rect y="30" width="48" height="7" rx="2" fill="#fff"/></svg>
    <h1>Welcome back, Ravi</h1>
  </header>

  <section class="profile" role="img" aria-label="Photo of a glass office building facade">
    <div class="avatar" role="img" aria-label="Profile photo of the user"></div>
    <div class="name">Ravi Tolland</div>
    <div class="location">
      <svg width="16" height="26" viewBox="0 0 16 26"><path d="M8 0a8 8 0 0 0-8 8c0 6 8 18 8 18s8-12 8-18a8 8 0 0 0-8-8z" fill="#000"/><circle cx="8" cy="8" r="3" fill="#fff"/></svg>
      San Francisco, CA
    </div>
    <div class="score">
      <span class="label">Score</span>
      <span class="value">650</span>
      <svg width="26" height="44" viewBox="0 0 26 44" style="margin-left:6px"><path d="M8 0h10v28h8L13 44 0 28h8z" fill="var(--down)" stroke="#7a1b1b" stroke-width="1"/></svg>
      <span class="delta">-18</span>
    </div>
  </section>

  <section class="week-stats">
    <div class="stat" style="left:32px">
      <div class="num">34%<svg width="20" height="28" viewBox="0 0 20 28" style="margin:0 4px"><path d="M10 0l10 12h-6v16H6V12H0z" fill="var(--up)"/></svg>+4</div>
      <div class="cap" style="left:3px">Completion</div>
    </div>
    <div class="sep" style="left:222px"></div>
    <div class="stat" style="left:250px">
      <div class="num">20<svg width="20" height="28" viewBox="0 0 20 28" style="margin:0 4px"><path d="M10 0l10 12h-6v16H6V12H0z" fill="var(--up)"/></svg>+3</div>
      <div class="cap" style="left:-1px">Sessions</div>
    </div>
    <div class="stat" style="left:393px">
      <div class="num">18<svg width="20" height="28" viewBox="0 0 20 28" style="margin:0 4px"><path d="M10 0l10 12h-6v16H6V12H0z" fill="var(--up)"/></svg>+10</div>
      <div class="cap" style="left:12px">Min.</div>
    </div>
    <div class="sep" style="left:526px"></div>
    <div class="stat" style="left:538px">
      <div class="cap">This week</div>
    </div>
  </section>
  <div class="progress"></div>
  <div class="progress-rest"></div>

  <section class="quick-links">
    <div class="bubble-btn btn-analytics"><span>Analytics</span><svg width="26" height="14" viewBox="0 0 26 14"><path d="M2 12L13 3l11 9" stroke="rgba(255,255,255,0.75)" stroke-width="3" fill="none"/></svg></div>
    <div class="bubble-btn btn-course"><span>Course<br>Overview</span><svg width="26" height="14" viewBox="0 0 26 14"><path d="M2 12L13 3l11 9" stroke="rgba(255,255,255,0.75)" stroke-width="3" fill="none"/></svg></div>
    <div class="bubble-btn btn-days"><span>Days until<br>test 33</span><svg width="26" height="14" viewBox="0 0 26 14"><path d="M2 12L13 3l11 9" stroke="rgba(255,255,255,0.75)" stroke-width="3" fill="none"/></svg></div>
  </section>
  <div class="rule" style="top:825px"></div>

  <div class="up-next">
    <svg width="452" height="162" viewBox="0 0 452 162" style="position:absolute;left:0;top:0">
      <path d="M40 0h356a40 40 0 0 1 40 40v56c0 14 6 30 16 50-22-6-36-14-46-22a40 40 0 0 1-10 16H40A40 40 0 0 1 0 100V40A40 40 0 0 1 40 0z" fill="var(--coral)"/>
    </svg>
    <div class="text">
      <div class="kicker">Up Next: Sentence Correction</div>
      <div class="lesson">Lesson 4</div>
    </div>
  </div>
  <div class="rule" style="top:1061px"></div>

  <nav class="tab-bar">
    <div class="tab" style="left:26px">
      <svg width="56" height="56" viewBox="0 0 56 56"><rect x="4" y="6" width="48" height="9" rx="2" fill="#555"/><rect x="0" y="20" width="50" height="9" rx="2" fill="#666"/><rect x="6" y="34" width="46" height="9" rx="2" fill="#555"/><rect x="2" y="46" width="50" height="9" rx="2" fill="#666"/></svg>
      <div class="label">Theory</div>
    </div>
    <div class="tab" style="left:154px">
      <svg width="56" height="58" viewBox="0 0 56 58"><rect x="8" y="6" width="40" height="50" rx="3" fill="none" stroke="#666" stroke-width="3"/><rect x="18" y="0" width="20" height="10" rx="2" fill="#666"/><path d="M16 22h24M16 30h24M16 38h24M16 46h16" stroke="#666" stroke-width="3"/></svg>
      <div class="label">Practice</div>
    </div>
    <div class="tab active" style="left:288px">
      <svg width="56" height="56" viewBox="0 0 56 56"><path d="M28 4L2 28h8v24h14V36h8v16h14V28h8L44 17V6h-7v5z" fill="#fff"/></svg>
      <div class="label">Home</div>
    </div>
    <div class="tab" style="left:421px">
      <svg width="60" height="50" viewBox="0 0 60 50"><path d="M12 8h36c8 0 12 10 12 24 0 12-8 14-14 6l-4-6H18l-4 6c-6 8-14 6-14-6C0 18 4 8 12 8z" fill="#666"/><path d="M14 18v12M8 24h12" stroke="#111" stroke-width="4"/><circle cx="44" cy="20" r="3" fill="#111"/><circle cx="38" cy="27" r="3" fill="#111"/></svg>
      <div class="label">Games</div>
    </div>
    <div class="tab" style="left:560px">
      <svg width="56" height="58" viewBox="0 0 56 58"><rect x="4" y="6" width="40" height="50" fill="none" stroke="#666" stroke-width="3"/><path d="M12 20h24M12 28h24M12 36h24M12 44h16" stroke="#666" stroke-width="3"/><path d="M34 8l6 6 12-14" stroke="#888" stroke-width="4" fill="none"/></svg>
      <div class="label">Test</div>
    </div>
  </nav>
</body>
</html>
```